Falcrest security business card

Looking for a business card for my security company

Target Market(s)

Security

Industry/Entity Type

Security

Contact Information for Business Card

Name - Gil Marston. Title - General manager - direct 314 862.4490 website www. falcrestsecurityservices.example email - gil@ falcrestsecurityservices.example

Requirements
Must have
• Logo attached

```html
<!DOCTYPE html>
<html lang="en">
<head>
<meta charset="utf-8">
<title>Falcrest Security Services – Business Card</title>
<link href="https://fonts.googleapis.com/css2?family=Roboto:wght@400;700&display=swap" rel="stylesheet">
<style>
  :root {
    --backdrop: #2b2c30;
    --card: #0d0d0e;
    --card-edge: #c9a445;
    --gold: #d4aa4f;
    --ink-light: #f2f2f2;
  }
  html, body {
    margin: 0;
    padding: 0;
    width: 1200px;
    height: 913px;
    overflow: hidden;
    background: var(--backdrop);
    font-family: "Roboto", Arial, sans-serif;
  }
  .canvas {
    position: relative;
    width: 1200px;
    height: 913px;
  }
  .card {
    position: absolute;
    width: 540px;
    height: 310px;
    background: var(--card);
    border: 2px solid var(--card-edge);
    border-radius: 18px;
    box-sizing: border-box;
    overflow: hidden;
  }
  .card--front { left: 70px; top: 90px; }
  .card--back  { left: 590px; top: 500px; }

  .brand-name {
    font-family: "Roboto", Arial, sans-serif;
    font-weight: 700;
    color: var(--gold);
    text-transform: uppercase;
    letter-spacing: 2px;
    display: flex;
    align-items: center;
    gap: 12px;
    margin: 0;
  }
  .brand-name__mark {
    display: inline-block;
    background: var(--gold);
    border-radius: 50%;
  }
  .card--front .brand-name {
    position: absolute;
    left: 0; right: 0; top: 0; bottom: 0;
    justify-content: center;
    font-size: 52px;
  }
  .card--front .brand-name__mark { width: 18px; height: 18px; }

  .card--back .brand-name {
    position: absolute;
    right: 34px;
    top: 44px;
    font-size: 32px;
  }
  .card--back .brand-name__mark { width: 12px; height: 12px; }

  .contact {
    position: absolute;
    left: 36px;
    bottom: 30px;
  }
  .contact__name {
    margin: 0;
    color: var(--gold);
    font-weight: 700;
    font-size: 22px;
    text-transform: uppercase;
    letter-spacing: 0.5px;
  }
  .contact__title {
    margin: 2px 0 12px;
    color: var(--ink-light);
    font-size: 17px;
  }
  .contact__list {
    list-style: none;
    margin: 0;
    padding: 0;
  }
  .contact__item {
    display: flex;
    align-items: center;
    gap: 8px;
    color: var(--ink-light);
    font-size: 16px;
    line-height: 24px;
  }
  .contact__icon {
    width: 13px;
    height: 13px;
    flex: none;
  }
</style>
</head>
<body>
<main class="canvas">
  <section class="card card--front" aria-label="Card front">
    <h1 class="brand-name"><span class="brand-name__mark"></span>Falcrest</h1>
  </section>

  <section class="card card--back" aria-label="Card back">
    <h2 class="brand-name"><span class="brand-name__mark"></span>Falcrest</h2>
    <div class="contact">
      <p class="contact__name">Gil Marston</p>
      <p class="contact__title">General manager</p>
      <ul class="contact__list">
        <li class="contact__item">
          <svg class="contact__icon" viewBox="0 0 16 16" aria-hidden="true"><path fill="#d4aa4f" d="M3.5 1l2.5 3-1.5 1.8a9 9 0 0 0 5.7 5.7L12 10l3 2.5-1.6 2.3C7.5 15 1 8.5 1.2 2.6z"/></svg>
          314 862.4490
        </li>
        <li class="contact__item">
          <svg class="contact__icon" viewBox="0 0 16 16" aria-hidden="true"><rect x="1" y="3" width="14" height="10" rx="1" fill="#d4aa4f"/><path d="M1.5 3.8L8 9l6.5-5.2" stroke="#0d0d0e" stroke-width="1.3" fill="none"/></svg>
          gil@ falcrestsecurityservices.example
        </li>
        <li class="contact__item">
          <svg class="contact__icon" viewBox="0 0 16 16" aria-hidden="true"><circle cx="8" cy="8" r="7" fill="#d4aa4f"/><path d="M1 8h14M8 1c-3 3.5-3 10.5 0 14M8 1c3 3.5 3 10.5 0 14" stroke="#0d0d0e" stroke-width="1.1" fill="none"/></svg>
          www. falcrestsecurityservices.example
        </li>
      </ul>
    </div>
  </section>
</main>
</body>
</html>
```